Real Estate For Sale Sign

I need to design a for sale sign. It needs to include The following information
Logo: Attached
Name: Corinne Vasquel,
Company Name: Gilded Harbor Real Estate,
Phone Number: 503-841-2096
BRE Licence Number 04817359 (Can Be small)
Sign size 24x30

I am not sure about including my website but I would like to see options with it. www.gildedharbor-example.com
Updates

Target Market(s)

Potential Buyers or Sellers of Real Estate. Must be easy to read.

Industry/Entity Type

Real Estate

Requirements
Must have
• I want it to feel luxurious and sharp.

```html
<!DOCTYPE html>
<html lang="en">
<head>
<meta charset="utf-8">
<title>Gilded Harbor Real Estate – For Sale Sign</title>
<link rel="stylesheet" href="https://fonts.googleapis.com/css2?family=Inter:wght@300;400&display=swap">
<style>
  :root {
    --backdrop: #aea18a;
    --sign-white: #ffffff;
    --sign-navy: #00285a;
    --brand-blue: #2361a8;
    --accent-cyan: #1ea6ea;
    --ink: #111111;
    --text-light: #ffffff;
  }
  * { margin: 0; padding: 0; box-sizing: border-box; }
  html, body {
    width: 1200px;
    height: 1200px;
    overflow: hidden;
    background: var(--backdrop);
    font-family: "Inter", Arial, sans-serif;
  }
  .canvas {
    position: relative;
    width: 1200px;
    height: 1200px;
  }
  .size-label {
    position: absolute;
    left: 36px;
    top: 30px;
    font-size: 38px;
    font-weight: 400;
    line-height: 1;
    color: var(--ink);
    letter-spacing: 1px;
  }
  .sign {
    position: absolute;
    left: 196px;
    top: 101px;
    width: 809px;
    height: 996px;
    background: var(--sign-navy);
    box-shadow: 8px 10px 12px rgba(0, 0, 0, 0.35);
  }
  .sign-header {
    position: absolute;
    left: 0;
    top: 0;
    width: 100%;
    height: 299px;
    background: var(--sign-white);
  }
  .brand-mark {
    position: absolute;
    left: 64px;
    top: 47px;
    width: 220px;
    height: 220px;
  }
  .brand-name {
    position: absolute;
    left: 300px;
    top: 92px;
    font-size: 50px;
    font-weight: 400;
    line-height: 1.12;
    color: var(--brand-blue);
    letter-spacing: 0.5px;
  }
  .headline {
    position: absolute;
    left: 178px;
    font-size: 206px;
    font-weight: 300;
    line-height: 1;
    color: var(--text-light);
    letter-spacing: -2px;
  }
  .headline--for { top: 331px; }
  .headline--sale { top: 518px; }
  .contact {
    position: absolute;
    left: 183px;
    line-height: 1;
    white-space: nowrap;
  }
  .contact--agent { top: 765px; font-size: 53px; color: var(--accent-cyan); }
  .contact--phone { top: 823px; font-size: 66px; color: var(--text-light); }
  .contact--web { top: 898px; font-size: 38px; color: var(--text-light); }
  .contact--licence { top: 953px; font-size: 16px; color: var(--text-light); }
</style>
</head>
<body>
  <main class="canvas">
    <div class="size-label">32x26</div>
    <section class="sign">
      <header class="sign-header">
        <svg class="brand-mark" viewBox="0 0 220 220" aria-hidden="true">
          <circle cx="110" cy="110" r="96" fill="none" stroke="#2f8fd6" stroke-width="8"/>
        </svg>
        <div class="brand-name">Gilded Harbor<br>Real Estate</div>
      </header>
      <div class="headline headline--for">For</div>
      <div class="headline headline--sale">Sale</div>
      <div class="contact contact--agent">Corinne Vasquel</div>
      <div class="contact contact--phone">503-841-2096</div>
      <div class="contact contact--web">www.gildedharbor-example.com</div>
      <div class="contact contact--licence">BRE Licence Number: 04817359</div>
    </section>
  </main>
</body>
</html>
```